Marketing fliers revised for 2024 Climb Onward

We are currently in the process of revitalizing our marketing fliers for the year 2024. Our leadership team has expressed their desire for a rejuvenated appearance for the upcoming year. In order to achieve this, we are seeking a different layout that effectively incorporates the same information.

To provide an example, the CEO has created a mock-up of the program, and I've attached the current flier, It is important to emphasize that we are aiming for a completely new and refreshed look.

This is our company website https://www.bayheronstock.example/

Target Market(s)

customers who buy roofing material

Industry/Entity Type

roofing and window

Colors
0054AA
0677BA
7BADD7
CADEEF
E8F1F8
0094D4
00A9DD
6FCCEA
C7EBF8
E9F6FB

Requirements
Must have
• all the details on the flier with a new look
Should not have
• the same look of he old flier

```html
<!DOCTYPE html>
<html lang="en">
<head>
<meta charset="utf-8">
<title>Climb Onward / Hold Steady 2024</title>
<link href="https://fonts.googleapis.com/css2?family=League+Spartan:wght@600;700;800&family=Poppins:wght@400;500;600&family=Bebas+Neue&family=Josefin+Sans:wght@600;700&display=swap" rel="stylesheet">
<style>
  :root{
    --page:#e6e8eb;
    --navy:#0c1a5f;
    --navy-deep:#091650;
    --orange:#f7a823;
    --sky-blue:#5aa9f0;
    --tag-blue:#3d7fe6;
    --white:#ffffff;
    --ink:#15151f;
  }
  *{margin:0;padding:0;box-sizing:border-box}
  html,body{width:1200px;height:2392px;overflow:hidden;background:var(--page)}
  .flyer{
    position:absolute;left:0;top:420px;width:1200px;height:1552px;
    background:var(--navy);overflow:hidden;
    font-family:"Poppins",sans-serif;color:var(--white);
    box-shadow:0 10px 40px rgba(0,0,0,.25);
  }
  .hero-photo{
    position:absolute;left:0;top:0;width:1200px;height:920px;
    background:linear-gradient(180deg,#6560b5 0%,#7d68b4 18%,#c77c8c 30%,#e8904f 38%,#9a6a95 47%,#3a2f6e 58%,#1a2268 72%,var(--navy) 100%);
  }
  .badge-back{
    position:absolute;left:934px;top:57px;width:206px;height:206px;border-radius:50%;
    background:#0e0e12;display:flex;align-items:center;justify-content:center;
    font-family:"League Spartan",sans-serif;font-weight:800;color:var(--orange);
    font-size:44px;line-height:.95;text-align:center;transform:rotate(-14deg);
  }
  .year{
    position:absolute;left:640px;top:300px;font-family:"Poppins",sans-serif;font-weight:500;
    font-size:262px;line-height:1;color:var(--ink);transform:scaleX(.74);transform-origin:left top;
    letter-spacing:-4px;
  }
  .headline{
    position:absolute;left:64px;top:400px;font-family:"League Spartan",sans-serif;font-weight:700;
    font-size:150px;line-height:123px;letter-spacing:-2px;white-space:nowrap;
  }
  .headline .accent{color:var(--orange)}
  .offer-line{
    position:absolute;left:66px;top:812px;font-family:"Josefin Sans",sans-serif;font-weight:700;
    font-size:38px;letter-spacing:2.5px;white-space:nowrap;
  }
  .offer-line .amount{color:var(--sky-blue);font-size:58px;margin-left:20px;letter-spacing:1px;vertical-align:-4px}
  .tier{
    position:absolute;top:917px;width:238px;height:124px;border:3px solid var(--tag-blue);border-radius:8px;
    text-align:center;
  }
  .tier.gold{border-color:var(--orange)}
  .tier .tag{
    position:absolute;left:26px;top:-28px;width:186px;height:40px;border-radius:8px;background:var(--tag-blue);
    font-weight:500;font-size:22px;line-height:40px;color:var(--white);
  }
  .tier.gold .tag{background:var(--orange);color:var(--navy-deep)}
  .tag sup{font-size:12px}
  .tier .label{margin-top:28px;font-size:24px;letter-spacing:6px;line-height:30px}
  .tier .value{font-family:"League Spartan",sans-serif;font-weight:700;font-size:60px;line-height:56px;color:var(--orange)}
  .tier.gold .value{color:var(--sky-blue)}
  .tier .value sup{font-size:30px;vertical-align:22px}
  .stay-row{
    position:absolute;left:76px;top:1072px;font-family:"Bebas Neue",sans-serif;font-size:66px;line-height:66px;white-space:nowrap;
  }
  .stay-row .program{color:var(--sky-blue);margin-right:44px}
  .stay-row .amount{color:var(--orange)}
  .bonus-bar{
    position:absolute;left:62px;top:1168px;width:1076px;height:116px;border:3px solid var(--orange);border-radius:14px;
  }
  .bonus-bar .level{
    position:absolute;left:-3px;top:-3px;width:436px;height:116px;background:var(--orange);border-radius:14px 0 0 14px;
    padding:18px 0 0 28px;
  }
  .level .small{font-size:22px;letter-spacing:4px;line-height:26px;color:var(--white)}
  .level .big{font-family:"League Spartan",sans-serif;font-weight:700;font-size:50px;line-height:54px;color:var(--navy-deep);white-space:nowrap}
  .bonus-bar .extra{position:absolute;left:466px;top:18px}
  .extra .main{font-weight:600;font-size:40px;line-height:46px;letter-spacing:1px}
  .extra .main span{color:var(--orange)}
  .extra .sub{font-size:22px;line-height:30px}
  .invite{
    position:absolute;left:68px;top:1313px;font-family:"Poppins",sans-serif;font-weight:600;font-size:22.5px;color:var(--orange);white-space:nowrap;
  }
  .brand-mark{
    position:absolute;left:63px;top:1400px;width:230px;height:60px;
    font-family:"League Spartan",sans-serif;font-weight:700;font-size:32px;line-height:60px;color:var(--white);white-space:nowrap;
  }
  .terms{position:absolute;left:307px;top:1369px;width:832px;font-size:12.6px;line-height:14px}
  .terms strong{color:var(--orange);font-weight:600}
  .handle{position:absolute;right:105px;top:1476px;font-size:20px}
</style>
</head>
<body>
<main class="flyer">
  <div class="hero-photo" role="img" aria-label="Sunset sky over a grassy hill with a silhouetted person leaping toward a jet airliner flying through a large red map pin"></div>
  <div class="badge-back">IT'S<br>BACK</div>
  <div class="year">2024</div>
  <h1 class="headline">CLIMB<br>ONWARD/<br><span class="accent">HOLD STEADY</span></h1>

  <p class="offer-line">NEW CUSTOMERS RECEIVE UP TO<span class="amount">$2,000</span></p>

  <div class="tier" style="left:68px"><div class="tag">BUY <sup>$</sup>10,000</div><div class="label">RECEIVE</div><div class="value"><sup>$</sup>500</div></div>
  <div class="tier gold" style="left:345px"><div class="tag">BUY <sup>$</sup>25,000</div><div class="label">RECEIVE</div><div class="value"><sup>$</sup>500</div></div>
  <div class="tier" style="left:622px"><div class="tag">BUY <sup>$</sup>50,000</div><div class="label">RECEIVE</div><div class="value"><sup>$</sup>500</div></div>
  <div class="tier gold" style="left:893px"><div class="tag">BUY <sup>$</sup>50,000</div><div class="label">RECEIVE</div><div class="value"><sup>$</sup>500</div></div>

  <p class="stay-row"><span class="program">HOLD STEADY</span>RECEIVE AN ADDITIONAL <span class="amount">$1,000!</span></p>

  <div class="bonus-bar">
    <div class="level"><div class="small">COMPLETE ALL LEVELS OF</div><div class="big">CLIMB ONWARD</div></div>
    <div class="extra"><div class="main">For an additional <span>$1,000!</span></div><div class="sub">Just spend the same or more than the previous year</div></div>
  </div>

  <p class="invite">GIVE BAY HERON A TRY AND SEE WHAT OTHER CONTRACTORS HAVE DISCOVERED SINCE 1973.</p>

  <div class="brand-mark">Bay Heron Stock</div>

  <p class="terms"><strong>TERMS AND CONDITIONS:</strong> A new customer is a contractor that has purchased less than $2,000 with Bay Heron Stock in the past six (6) months from the time of the first eligible voucher. Materials must be paid. The customer has 12 months from the date of the first qualifying purchase to reach all levels of Climb Onward. If you reach all four levels of Climb Onward, you are then eligible for Hold Steady. Hold Steady voucher may be rewarded when you match or beat the previous year purchase. The vouchers are to be used toward future purchases but may not be used to pay off previous balance on the customer's account. No one-time purchasers. This promotion and your participation in it is void where prohibited by law, rules or regulations. Bay Heron Stock reserves the right to cancel, suspend, and/or modify this promotion at any time, for any reason, without prior notice. Vouchers are valid up to one year after issued date. Promotion expires December 31, 2024. All rights reserved by Bay Heron Stock.</p>

  <p class="handle">@bayheronstock</p>
</main>
</body>
</html>
```